Business Card Design Project

We need a business card for a chiropractic and rehabilitation center. We already have a logo and need the card to follow the color and feel of the logo.

Target Market(s)

adults 30-55 that have some ache or pain that is interfering with their life, so much as they are ready to do something about it.

Industry/Entity Type

Business

```html
<!DOCTYPE html>
<html lang="en">
<head>
<meta charset="utf-8">
<title>Corespine Business Card</title>
<link href="https://fonts.googleapis.com/css2?family=Open+Sans:wght@400;600;700&display=swap" rel="stylesheet">
<style>
  :root {
    --backdrop: #3b3b3b;
    --card-white: #ffffff;
    --ink-dark: #454548;
    --ink-muted: #7a7a7c;
    --accent-orange: #e5900f;
    --grad-start: #e4920f;
    --grad-mid: #cf521b;
    --grad-end: #ae0d1b;
    --on-accent: #ffffff;
  }
  * { margin: 0; padding: 0; box-sizing: border-box; }
  html, body {
    width: 1200px;
    height: 907px;
    overflow: hidden;
    background: var(--backdrop);
    font-family: "Open Sans", Arial, sans-serif;
  }
  .card {
    position: absolute;
    top: 155px;
    width: 381px;
    height: 622px;
    border-radius: 21px;
    overflow: hidden;
  }
  .card--front { left: 191px; background: var(--card-white); }
  .card--back {
    left: 634px;
    background: linear-gradient(150deg, var(--grad-start) 0%, var(--grad-mid) 55%, var(--grad-end) 100%);
  }
  .brand__name {
    position: absolute;
    font-size: 40px;
    font-weight: 600;
    letter-spacing: 2px;
    line-height: 1;
    white-space: nowrap;
  }
  .card--front .brand__name { top: 172px; left: 68px; color: var(--ink-dark); }
  .card--back .brand__name { top: 297px; left: 66px; color: var(--on-accent); }
  .contact__name {
    position: absolute;
    top: 320px;
    left: 68px;
    font-size: 27px;
    font-weight: 700;
    color: var(--accent-orange);
    line-height: 1;
  }
  .contact__role {
    position: absolute;
    top: 349px;
    left: 68px;
    font-size: 18px;
    color: var(--ink-muted);
  }
  .contact__details {
    position: absolute;
    top: 461px;
    left: 68px;
    font-size: 18px;
    line-height: 21.5px;
    color: var(--ink-muted);
    list-style: none;
  }
</style>
</head>
<body>
  <section class="card card--front" aria-label="Card front">
    <span class="brand__name">CORESPINE</span>
    <h1 class="contact__name">LENA MARSH</h1>
    <p class="contact__role">Director of Sales &amp; Marketing</p>
    <ul class="contact__details">
      <li>#2210 - 118 Harbour Ave.</li>
      <li>Northvale, B.C. V2K4P7 Canada</li>
      <li>Phone: 604 555 0138</li>
      <li>lena@corespinerehab.com</li>
    </ul>
  </section>

  <section class="card card--back" aria-label="Card back">
    <span class="brand__name">CORESPINE</span>
  </section>
</body>
</html>
```